Need a new letterhead

Need a new fresh exciting letterhead. Remove the footer...info is outdated.

Target Market(s)

B2B

Industry/Entity Type

Electrical Power

Colors

Designer to choose colors to be used in the design.

Requirements
Must have
• Red and Blue Brindlecroft Arcwell Logo
Nice to have
• Lighting the way to sustainability in footer...reorganize the words?

```html
<!DOCTYPE html>
<html lang="en">
<head>
<meta charset="utf-8">
<title>Brindlecroft Arcwell — Letterhead</title>
<link href="https://fonts.googleapis.com/css2?family=Lato:wght@400;700;900&display=swap" rel="stylesheet">
<style>
  :root {
    --backdrop: #c9bdb8;
    --paper: #fffffb;
    --brand-red: #e8202a;
    --brand-blue: #243a8f;
    --ray-tint: #fbf6e6;
    --leaf-tint: #eef3ea;
  }
  * { box-sizing: border-box; margin: 0; padding: 0; }
  html, body {
    width: 1200px; height: 784px; overflow: hidden;
    background: var(--backdrop);
    font-family: "Lato", Arial, sans-serif;
  }
  .letterhead {
    position: absolute;
    left: 314px; top: 22px;
    width: 572px; height: 740px;
    background: var(--paper);
    box-shadow: 0 2px 10px rgba(0,0,0,0.12);
  }
  .brand-name {
    position: absolute;
    left: 44px; top: 40px;
    color: var(--brand-red);
    font-weight: 900;
    font-size: 26px;
    line-height: 1.0;
    text-transform: uppercase;
    letter-spacing: 0.5px;
  }
  .contact {
    position: absolute;
    right: 40px; top: 150px;
    text-align: left;
    font-size: 10px;
    line-height: 1.45;
  }
  .contact .address { color: var(--brand-red); }
  .contact .line { display: flex; align-items: center; gap: 5px; color: var(--brand-blue); }
  .contact svg { width: 8px; height: 8px; flex: none; }
  .watermark {
    position: absolute;
    left: 106px; top: 200px;
    width: 360px; height: 300px;
    border-radius: 50%;
    background: radial-gradient(circle, var(--leaf-tint) 0%, var(--leaf-tint) 35%, var(--ray-tint) 60%, rgba(255,255,251,0) 75%);
  }
  .tagline {
    position: absolute;
    left: 0; right: 0; bottom: 36px;
    text-align: center;
    color: var(--brand-red);
    font-size: 12px;
    letter-spacing: 0.3px;
    text-transform: uppercase;
  }
</style>
</head>
<body>
  <main class="letterhead">
    <div class="brand-name">Brindlecroft<br>Arcwell</div>

    <address class="contact" style="font-style: normal;">
      <div class="address">417 Harrow Lane<br>Fenwick, Ohio 43210</div>
      <div class="line">
        <svg viewBox="0 0 10 10" aria-hidden="true"><path d="M2 1 L4 1 L4.6 3.2 L3.4 4 Q4.3 5.8 6 6.6 L6.8 5.4 L9 6 L9 8 Q9 9 8 9 Q1 8.5 1 2 Q1 1 2 1Z" fill="var(--brand-red)"/></svg>
        555-014-2290
      </div>
      <div class="line">
        <svg viewBox="0 0 10 10" aria-hidden="true"><path d="M2 1 L4 1 L4.6 3.2 L3.4 4 Q4.3 5.8 6 6.6 L6.8 5.4 L9 6 L9 8 Q9 9 8 9 Q1 8.5 1 2 Q1 1 2 1Z" fill="var(--brand-red)"/></svg>
        555-014-2291
      </div>
      <div class="line">
        <svg viewBox="0 0 10 10" aria-hidden="true"><circle cx="5" cy="5" r="4" fill="none" stroke="var(--brand-red)" stroke-width="1.2"/><path d="M1 5 H9 M5 1 Q2.5 5 5 9 M5 1 Q7.5 5 5 9" fill="none" stroke="var(--brand-red)" stroke-width="0.8"/></svg>
        www.BrindlecroftArcwell.com
      </div>
    </address>

    <div class="watermark" role="img" aria-label="Faint background emblem: recycling arrows inside a ring of sun rays with a light bulb"></div>

    <p class="tagline">Lighting the way to sustainability</p>
  </main>
</body>
</html>
```